Business Card Design

We need a business card simular to the previous but including our logo our colours are royal blue, silver and black. we currently need cards for
Doug Pemberley Sales Manager 0400 295 617
doug@ridgelinegatesystems.com.au
Renee Blackwater 0415 832 190
renee@ridgelinegatesystems.com.au
Address 7 / 4 Marunga St Lonsdale
WEB www.ridgelinegatesystems.com.au
PH 84157203 Fax: 84157219
Updates
Good Morning all, I really don't like so much white. On the back I would like a list of all our products Security Doors & Screens, Built in Robes, Shower Screens, Blinds, Awnings, Roller Shutters & More Appointment Date & Time. Cheers Renee
Industry/Entity Type
Royal
Contact Information for Business Card
I really like the writing on our last business card from Cardmill.
Ridgeline Gate Systems , Factory Direct Prices, No Obligation Free Measure & Quote. List of Products Security Doors & Windows, Built in Robes, Indoor & Outdoor Blinds Inc Awnings & Velafolds, Shower Screens, Roller Shutters and More.
Font styles to use

```html
<!DOCTYPE html>
<html lang="en">
<head>
<meta charset="utf-8">
<title>Ridgeline Gate Systems – Business Card</title>
<link href="https://fonts.googleapis.com/css2?family=Open+Sans:wght@400;600;700&display=swap" rel="stylesheet">
<style>
  :root {
    --backdrop: #1c1c1e;
    --card-black: #050505;
    --royal-blue: #0f57a8;
    --silver: #c9ccd1;
    --white: #ffffff;
    --ink: #111111;
  }
  * { box-sizing: border-box; margin: 0; padding: 0; }
  html, body {
    width: 914px; height: 1200px; overflow: hidden;
    background: var(--backdrop);
    font-family: "Open Sans", Arial, sans-serif;
  }
  .sheet {
    width: 914px; height: 1200px;
    display: flex; flex-direction: column; align-items: center; justify-content: center;
    gap: 72px;
  }
  .card {
    width: 760px; height: 434px;
    background: var(--card-black);
    position: relative; overflow: hidden;
    box-shadow: 0 10px 30px rgba(0,0,0,0.55);
  }
  .brand {
    display: flex; align-items: center; justify-content: center; gap: 18px;
  }
  .brand-mark {
    width: 56px; height: 56px; border-radius: 50%;
    background: linear-gradient(145deg, #f2f3f5, var(--silver) 55%, #8d9096);
    border: 3px solid var(--royal-blue);
  }
  .brand-name {
    font-weight: 700; font-size: 38px; color: var(--white);
    line-height: 1.1; letter-spacing: 0.5px;
  }

  /* Front */
  .front-top { height: 172px; display: flex; align-items: center; justify-content: center; }
  .front-bottom {
    position: absolute; left: 0; right: 0; bottom: 0; top: 172px;
    background: var(--royal-blue); color: var(--white);
    text-align: center; padding-top: 24px;
    font-size: 21px; line-height: 1.35;
  }
  .person { font-size: 25px; margin-bottom: 12px; }
  .person strong { font-weight: 700; }
  .contact-line { display: flex; justify-content: center; align-items: center; gap: 10px; margin-bottom: 10px; }
  .contact-line .gap { width: 40px; }
  .icon { width: 22px; height: 22px; fill: var(--white); flex: none; }
  .address { font-size: 20px; margin-top: 6px; }
  .tagline { font-size: 20px; }

  /* Back */
  .back-top { height: 150px; display: flex; align-items: center; justify-content: center; }
  .back-rule { position: absolute; top: 150px; left: 0; right: 0; height: 5px; background: var(--royal-blue); }
  .products {
    position: absolute; top: 190px; left: 80px; right: 80px;
    color: var(--white); text-align: center; text-transform: uppercase;
    font-size: 23px; line-height: 1.3;
  }
  .appointment {
    position: absolute; left: 0; right: 0; bottom: 0; height: 74px;
    background: var(--white); color: var(--ink);
    display: flex; align-items: center; padding-left: 64px;
    font-size: 22px; text-transform: uppercase;
  }
  .appointment .time { margin-left: auto; margin-right: 150px; }
</style>
</head>
<body>
<main class="sheet">
  <section class="card card-front">
    <div class="front-top">
      <div class="brand"><span class="brand-mark"></span><span class="brand-name">Ridgeline Gate Systems</span></div>
    </div>
    <div class="front-bottom">
      <p class="person"><strong>Doug Pemberley</strong>, Sales Manager 0400 295 617</p>
      <p class="contact-line">
        <svg class="icon" viewBox="0 0 24 24"><path d="M2 5h20v14H2z" fill="none" stroke="#fff" stroke-width="2"/><path d="M2 5l10 8 10-8" fill="none" stroke="#fff" stroke-width="2"/></svg>
        doug@ridgelinegatesystems.com.au
      </p>
      <p class="contact-line">
        <svg class="icon" viewBox="0 0 24 24"><path d="M6.6 10.8a15 15 0 0 0 6.6 6.6l2.2-2.2a1 1 0 0 1 1-.25 11.4 11.4 0 0 0 3.6.6 1 1 0 0 1 1 1V20a1 1 0 0 1-1 1A17 17 0 0 1 3 4a1 1 0 0 1 1-1h3.5a1 1 0 0 1 1 1c0 1.25.2 2.45.6 3.6a1 1 0 0 1-.25 1z"/></svg>
        84157203
        <span class="gap"></span>
        <svg class="icon" viewBox="0 0 24 24"><path d="M3 8h4v13H3zM9 3h9v5H9zM8 9h14v12H8z"/><path d="M11 12h2v2h-2zM15 12h2v2h-2zM11 16h2v2h-2zM15 16h2v2h-2z" fill="#0f57a8"/></svg>
        84157219
      </p>
      <p class="address">7 / 4 Marunga St Brackenvale SA 5162</p>
      <p class="tagline">www.ridgelinegatesystems.com.au</p>
      <p class="tagline">Factory Direct Prices, No Obligation FREE MEASURE &amp; QUOTE</p>
    </div>
  </section>

  <section class="card card-back">
    <div class="back-top">
      <div class="brand"><span class="brand-mark"></span><span class="brand-name">Ridgeline Gate Systems</span></div>
    </div>
    <div class="back-rule"></div>
    <p class="products">Security Doors &amp; Windows, Built in Robes, Indoor &amp; Outdoor Blinds inc Awnings &amp; Velafolds, Shower Screens, Roller Shutters and More.</p>
    <div class="appointment"><span>Appointment Date:</span><span class="time">Time:</span></div>
  </section>
</main>
</body>
</html>
```